Game, Voice & Dedicated Server Company Needs a Business Card Design

We need a new business card design, centered around our new logo (PSD provided below).

Designs that we do like:
https://pixelmarsh.net/item/corporate-business-card/5382017?s_rank=43 (needs to be made more eye catching)

Our main areas of business are:
- Dedicated Servers
- Game Servers
- Voice Servers
- Mitigation Security Specialists

Industry/Entity Type

Business

Contact Information for Business Card

On the card: (and anything else you would suggest)
- Staff member name
- Staff member position in company
- Staff member phone number
- Staff member email
- Other / Staff member Skype
- Website link

Colors
9bcb3c
abd036

Requirements
Must have
• Design of Card:
• - Green (same green as the logo)
• - Business / Corporate design
• - Something a little different / abstract that shouts premium

```html
<!DOCTYPE html>
<html lang="en">
<head>
<meta charset="utf-8">
<title>Brightpath Hosting – Business Card</title>
<link rel="stylesheet" href="https://fonts.googleapis.com/css2?family=Lato:wght@400;700;900&display=swap">
<style>
  :root {
    --backdrop: #2b2b2b;
    --card-dark: #1f1f1f;
    --card-light: #f4f4f4;
    --brand-green: #9bcb3c;
    --brand-green-alt: #abd036;
    --ink-light: #d8d8d8;
    --ink-muted: #9a9a9a;
    --rule: #333333;
    --stripe-white: #ffffff;
    --stripe-black: #111111;
  }
  * { box-sizing: border-box; margin: 0; padding: 0; }
  html, body {
    width: 1200px; height: 873px; overflow: hidden;
    background: var(--backdrop);
    font-family: "Lato", sans-serif;
  }
  .canvas { position: relative; width: 1200px; height: 873px; }

  .card {
    position: absolute; width: 560px; height: 320px;
    border-radius: 18px; overflow: hidden;
    box-shadow: 0 14px 30px rgba(0,0,0,.45);
  }

  /* Back of card */
  .card-back {
    left: 70px; top: 80px;
    background: var(--card-dark);
    display: flex; flex-direction: column; align-items: center; justify-content: center;
  }
  .card-back .texture {
    position: absolute; inset: 0;
    background: radial-gradient(ellipse at 40% 30%, #2c2c2c 0%, var(--card-dark) 70%);
  }
  .brand {
    position: relative; display: flex; align-items: center; gap: 16px;
    color: var(--brand-green); font-weight: 900; text-transform: uppercase;
    line-height: .95;
  }
  .brand-dot { border-radius: 50%; background: var(--brand-green); flex: none; }
  .card-back .brand { font-size: 36px; margin-bottom: 26px; }
  .card-back .brand-dot { width: 58px; height: 58px; }
  .services { position: relative; text-align: center; }
  .services-title {
    display: inline-block; color: var(--brand-green); font-weight: 700; font-size: 17px;
    border-bottom: 1px solid var(--brand-green); padding-bottom: 3px; margin-bottom: 12px;
  }
  .services-line { color: var(--ink-light); font-size: 17px; line-height: 1.6; }
  .services-line .sep { color: var(--ink-muted); margin: 0 8px; }

  /* Front of card */
  .card-front { left: 570px; top: 470px; background: var(--card-dark); display: flex; }
  .front-logo-panel {
    position: relative; width: 280px; height: 100%; flex: none;
    background: linear-gradient(135deg, #ffffff 0%, var(--card-light) 55%, #e4e4e4 100%);
    display: flex; align-items: center; justify-content: center;
  }
  .front-logo-panel .brand { flex-direction: column; gap: 18px; text-align: center; font-size: 33px; }
  .front-logo-panel .brand-dot { width: 80px; height: 80px; }
  .stripes { display: flex; height: 100%; flex: none; }
  .stripes span { width: 3px; height: 100%; }
  .stripes .w { background: var(--stripe-white); }
  .stripes .b { background: var(--stripe-black); }

  .contact-panel { flex: 1; min-width: 0; display: flex; flex-direction: column; }
  .person { text-align: center; padding: 22px 12px 14px; border-bottom: 1px solid var(--rule); }
  .person-name { color: var(--brand-green); font-weight: 700; font-size: 19px; }
  .person-role { color: var(--ink-muted); font-size: 12px; margin-top: 3px; }
  .contact-row {
    flex: 1; display: flex; align-items: center; gap: 12px; padding: 0 16px 0 16px;
    border-bottom: 1px solid var(--rule);
    color: var(--ink-light); font-size: 12.5px; line-height: 1.55;
  }
  .contact-row:last-child { border-bottom: none; }
  .contact-text { min-width: 0; white-space: nowrap; }
  .icon-ring {
    width: 40px; height: 40px; border-radius: 50%; flex: none;
    border: 2px solid #cfcfcf; display: flex; align-items: center; justify-content: center;
  }
  .icon-ring .icon-fill {
    width: 30px; height: 30px; border-radius: 50%; background: var(--brand-green);
    display: flex; align-items: center; justify-content: center;
  }
</style>
</head>
<body>
<main class="canvas">

  <section class="card card-back" aria-label="Back of business card">
    <div class="texture" role="img" aria-label="Faint dark low-poly texture"></div>
    <div class="brand"><span class="brand-dot"></span><span>Brightpath<br>Hosting</span></div>
    <div class="services">
      <div class="services-title">Main areas of Business are:</div>
      <div class="services-line">Dedicated Servers<span class="sep">/</span>Game Servers</div>
      <div class="services-line">Voice Servers<span class="sep">/</span>Mitigation Security Specialists</div>
    </div>
  </section>

  <section class="card card-front" aria-label="Front of business card">
    <div class="front-logo-panel" role="img" aria-label="Light grey low-poly background behind brand name">
      <div class="brand"><span class="brand-dot"></span><span>Brightpath<br>Hosting</span></div>
    </div>
    <div class="stripes"><span class="w"></span><span class="b"></span><span class="w"></span><span class="b"></span><span class="w"></span><span class="b"></span><span class="w"></span></div>
    <div class="contact-panel">
      <div class="person">
        <div class="person-name">Marcus Hale</div>
        <div class="person-role">CEO &amp; Managing Director</div>
      </div>
      <div class="contact-row">
        <span class="icon-ring"><span class="icon-fill">
          <svg width="18" height="18" viewBox="0 0 24 24" aria-hidden="true"><path fill="#1f1f1f" d="M6.6 10.8a15 15 0 0 0 6.6 6.6l2.2-2.2c.3-.3.7-.4 1-.2 1.1.4 2.3.6 3.6.6.6 0 1 .4 1 1V20c0 .6-.4 1-1 1A17 17 0 0 1 3 4c0-.6.4-1 1-1h3.5c.6 0 1 .4 1 1 0 1.3.2 2.5.6 3.6.1.3 0 .7-.2 1z"/></svg>
        </span></span>
        <span class="contact-text">02 7341 9260</span>
      </div>
      <div class="contact-row">
        <span class="icon-ring"><span class="icon-fill"></span></span>
        <span class="contact-text">Brightpath.Hosting</span>
      </div>
      <div class="contact-row">
        <span class="icon-ring"><span class="icon-fill">
          <svg width="18" height="14" viewBox="0 0 20 16" aria-hidden="true"><rect x="1" y="1" width="18" height="14" rx="1" fill="#1f1f1f"/><path d="M1.5 1.5 10 9l8.5-7.5" fill="none" stroke="#9bcb3c" stroke-width="1.5"/></svg>
        </span></span>
        <span class="contact-text">info@brightpathhosting.com<br>www.brightpathhosting.com</span>
      </div>
    </div>
  </section>

</main>
</body>
</html>
```